Website design with eCommerce for revolutionary new product in the manufacturing industry.

We need a website designed for a precision manufacturing company based in the suburbs of Minneapolis, Minnesota called Velk Manufacturing. We have a revolutionary new product, the TREMLA, to introduce and sell through an eCommerce storefront. The website would include company information, product information, and the storefront. Green is a color that represents Velk Manufacturing. The final design should communicate that we exclusively offer premium products at a premium price. The design should also let the customer know they are the focus of our work.

Target Market(s)

Machinists and machine shops

Industry/Entity Type

Manufacturing and machine shops

Coding

Coded - Design and coding required

Font styles to use
Sans Serif

Colors
59FF00
82FF00
B8FF75
E3FFCB
F4FFEA

Requirements
Must have
• eCommerce storefront, Made in USA references
Nice to have
• Home page, TREMLA Product page, About Us, Capabilities, Contact, etc.
Should not have
• Should not be too much text and reading.

```html
<!DOCTYPE html>
<html lang="en">
<head>
<meta charset="utf-8">
<title>Velk Manufacturing</title>
<link href="https://fonts.googleapis.com/css2?family=Outfit:wght@300;400;500;600;700;800&display=swap" rel="stylesheet">
<style>
:root{
  --green:#1b8a1b;
  --green-bright:#6cc23f;
  --ink:#111111;
  --text:#333333;
  --muted:#555555;
  --white:#ffffff;
  --line:#e2e2e2;
}
*{box-sizing:border-box;margin:0;padding:0}
html,body{width:1200px;height:3315px;overflow:hidden}
body{font-family:'Outfit',sans-serif;color:var(--text);background:var(--white);position:relative}
.abs{position:absolute}
.wordmark{font-weight:800;font-size:28px;letter-spacing:2px;color:var(--ink);display:flex;align-items:center;gap:8px}
.wordmark .sq{width:14px;height:14px;background:var(--ink)}

.site-header{position:absolute;top:0;left:0;width:1200px;height:71px;background:var(--white)}
.site-header .wordmark{position:absolute;left:158px;top:20px}
.main-nav{position:absolute;left:390px;top:29px;display:flex;gap:28px;font-size:12px;font-weight:500;color:var(--ink)}
.main-nav .active::before{content:"→ ";color:var(--green)}
.phone{position:absolute;left:917px;top:24px;font-weight:600;font-size:15px;color:var(--ink);display:flex;align-items:center;gap:8px}

.hero{position:absolute;top:71px;left:0;width:1200px;height:491px;background:linear-gradient(135deg,#2b2824,#14130f 60%,#24211d)}
.hero .ghost{position:absolute;left:155px;top:80px;font-size:84px;font-weight:800;letter-spacing:6px;color:rgba(255,255,255,.06)}
.hero h1{position:absolute;left:156px;top:180px;font-size:47px;line-height:48px;font-weight:800;color:var(--white);letter-spacing:.5px}
.hero h1 .accent{color:var(--green-bright)}
.hero p{position:absolute;left:158px;top:283px;width:380px;font-size:14px;line-height:19px;font-weight:500;color:var(--white)}
.btn-outline{position:absolute;border:1px solid var(--white);color:var(--white);font-size:12px;font-weight:500;display:flex;align-items:center;justify-content:center;border-radius:3px}
.hero .btn-outline{left:158px;top:348px;width:131px;height:38px}
.hero-photo{position:absolute;left:690px;top:48px}

.why{position:absolute;top:562px;left:0;width:1200px;height:377px;text-align:center}
.eyebrow{font-size:12px;color:var(--green);font-weight:400}
.section-title{font-size:21px;line-height:24px;font-weight:500;color:var(--ink);text-transform:uppercase}
.why .eyebrow{position:absolute;top:106px;width:1200px}
.why .section-title{position:absolute;top:134px;width:1200px}
.features{position:absolute;top:248px;left:157px;display:flex}
.feature{display:flex;align-items:center;gap:12px;width:328px;text-align:left;font-size:13px;line-height:15px;color:var(--muted)}
.feature .ic{width:60px;height:58px;border:1px solid var(--line);border-radius:4px;display:flex;align-items:center;justify-content:center}

.what{position:absolute;top:939px;left:0;width:1200px;height:375px;background:linear-gradient(120deg,#3e3a33,#2a2925 50%,#403c35)}
.what-title{position:absolute;left:158px;top:59px;font-size:21px;font-weight:500;color:var(--white);display:flex;align-items:center;gap:6px}
.what-title .accent{color:var(--green-bright)}
.what-copy{position:absolute;left:394px;top:57px;width:440px;font-size:16px;line-height:20px;font-weight:500;color:var(--white)}
.what .btn-outline{left:910px;top:53px;width:130px;height:36px}
.what .rule{position:absolute;left:0;top:122px;width:1200px;height:1px;background:rgba(255,255,255,.25)}
.gallery-head{position:absolute;top:148px;width:1200px;text-align:center}
.gallery-head .eyebrow{color:var(--green-bright)}
.gallery-head .section-title{color:var(--white);margin-top:6px}
.carousel-arrow{position:absolute;top:295px}
.shot{position:absolute;border-radius:3px}

.better{position:absolute;top:1556px;left:0;width:1200px;height:389px;background:linear-gradient(90deg,#e9e9e9,#f4f4f4)}
.better h2{position:absolute;left:595px;top:54px;font-size:21px;font-weight:500;color:var(--ink);display:flex;align-items:center;gap:8px}
.checks{position:absolute;left:597px;top:100px;width:420px;list-style:none}
.checks li{display:flex;gap:12px;font-size:12px;line-height:17px;color:var(--muted);margin-bottom:18px}
.checks svg{flex:none;margin-top:2px}
.btn-dark{position:absolute;left:598px;top:283px;width:130px;height:38px;background:var(--ink);color:var(--white);font-size:12px;font-weight:500;display:flex;align-items:center;justify-content:center;border-radius:3px}

.caps{position:absolute;top:1945px;left:0;width:1200px;height:734px;text-align:center}
.caps .eyebrow{position:absolute;top:65px;width:1200px}
.caps .section-title{position:absolute;top:89px;width:1200px}
.cap{position:absolute;width:290px;text-align:left}
.cap .ic{height:50px}
.cap h3{font-size:16px;font-weight:500;color:var(--ink);margin-top:16px;display:flex;align-items:center;gap:6px}
.cap h3::after{content:"";width:14px;height:1px;background:var(--green)}
.cap p{font-size:12px;line-height:15.5px;color:var(--muted);margin-top:8px;width:222px}
.cap .go{margin-top:12px}
.divider-v{position:absolute;width:1px;background:var(--line)}
.divider-h{position:absolute;height:1px;background:var(--line)}
.btn-green{position:absolute;background:var(--green);color:var(--white);font-size:13px;font-weight:500;display:flex;align-items:center;justify-content:center;border-radius:3px}

.contact{position:absolute;top:2679px;left:0;width:1200px;height:456px;background:linear-gradient(135deg,#262622,#151513 55%,#23231f)}
.contact h2{position:absolute;left:157px;top:64px;font-size:21px;font-weight:500;color:var(--white)}
.field{position:absolute;left:158px;width:325px;height:37px;border:1px solid rgba(255,255,255,.55);border-radius:3px;font-size:11px;color:rgba(255,255,255,.6);padding:11px 15px}
.contact .btn-green{left:158px;top:358px;width:110px;height:35px;font-size:12px}

.site-footer{position:absolute;top:3135px;left:0;width:1200px;height:180px;background:var(--white)}
.site-footer .wordmark{position:absolute;left:160px;top:55px}
.foot-nav{position:absolute;left:437px;top:65px;display:flex;gap:20px;font-size:11px;font-weight:500;color:var(--ink)}
.site-footer .rule{position:absolute;left:0;top:112px;width:1200px;height:1px;background:var(--line)}
.copyright{position:absolute;left:157px;top:136px;font-size:10px;color:var(--ink)}
.social{position:absolute;left:927px;top:131px;display:flex;gap:6px}
.social span{width:24px;height:24px;border-radius:50%;background:#cfcfcf}
.social span:first-child{background:var(--green)}
</style>
</head>
<body>

<header class="site-header">
  <div class="wordmark"><span class="sq"></span>TREMLA</div>
  <nav class="main-nav">
    <span class="active">HOME</span><span>CAPABILITIES</span><span>ABOUT US</span><span>GALLERY</span><span>WISDOM</span><span>CONTACT US</span>
  </nav>
  <div class="phone">
    <svg width="20" height="20" viewBox="0 0 24 24" fill="none" stroke="#111" stroke-width="2"><path d="M5 3h4l2 5-3 2a12 12 0 0 0 6 6l2-3 5 2v4a2 2 0 0 1-2 2A17 17 0 0 1 3 5a2 2 0 0 1 2-2z"/></svg>
    555 014 2271
  </div>
</header>

<section class="hero">
  <div class="ghost">TREMLA</div>
  <h1>WELCOME TO <span class="accent">VELK</span><svg width="52" height="20" viewBox="0 0 52 20" fill="none" stroke="#6cc23f" stroke-width="2"><path d="M0 7h40M0 13h40M38 2l12 8-12 8"/></svg><br>MANUFACTURING</h1>
  <p>We are a machine shop with complete end to end manufacturing capabilities.</p>
  <div class="btn-outline">SHOP NOW</div>
  <svg class="hero-photo" width="400" height="420" viewBox="0 0 400 420">
    <defs><linearGradient id="heroGrad" x1="0" y1="0" x2="1" y2="1"><stop offset="0" stop-color="#a9bfd0"/><stop offset=".5" stop-color="#3e5f80"/><stop offset="1" stop-color="#8a9aa6"/></linearGradient></defs>
    <polygon points="60,20 395,20 355,412 20,412" fill="none" stroke="#6cc23f" stroke-width="1.5"/>
    <polygon role="img" aria-label="Smiling machinist standing in a workshop" points="40,0 375,0 335,392 0,392" fill="url(#heroGrad)"/>
  </svg>
</section>

<section class="why">
  <svg class="abs" style="left:588px;top:33px" width="24" height="36" viewBox="0 0 24 36" fill="none" stroke="#222" stroke-width="1.5"><path d="M12 0v34M2 24l10 10 10-10"/></svg>
  <div class="eyebrow">Why Velk Manufacturing?</div>
  <h2 class="section-title">Because there is a better way, and we will find it,<br>even if it's the hard way.&nbsp; We believe in working<br>harder and smarter to achieve success.</h2>
  <div class="features">
    <div class="feature"><div class="ic"><svg width="30" height="30" viewBox="0 0 30 30" fill="none" stroke="#333" stroke-width="1.3"><path d="M3 27h24M7 27V18M12 27V14M17 27V10M22 27V6"/><circle cx="22" cy="3" r="1.5" stroke="#6cc23f"/></svg></div>Our success is measured<br>in your success</div>
    <div class="feature"><div class="ic"><svg width="30" height="30" viewBox="0 0 30 30" fill="none" stroke="#333" stroke-width="1.3"><circle cx="14" cy="16" r="11"/><circle cx="14" cy="16" r="6"/><circle cx="14" cy="16" r="1.5"/><path d="M14 16L26 4" stroke="#6cc23f"/></svg></div>Focused on our your needs<br>and making excellent parts</div>
    <div class="feature"><div class="ic"><svg width="30" height="30" viewBox="0 0 30 30" fill="none" stroke="#333" stroke-width="1.3"><path d="M3 27l7-9 5 5 7-10 5 14z"/><circle cx="22" cy="6" r="3" stroke="#6cc23f"/></svg></div>Exceeding your<br>expectations</div>
  </div>
</section>

<section class="what">
  <div class="what-title">WHAT WE <span class="accent">DO</span><svg width="50" height="18" viewBox="0 0 50 18" fill="none" stroke="#6cc23f" stroke-width="1.6"><path d="M0 6h38M0 12h38M36 2l12 7-12 7"/></svg></div>
  <p class="what-copy">We are a machine shop with complete end to end manufacturing capabilities.</p>
  <div class="btn-outline">LEARN MORE</div>
  <div class="rule"></div>
  <div class="gallery-head">
    <div class="eyebrow">Gallery</div>
    <h2 class="section-title">Here are some of the projects we've<br>created over the years.</h2>
  </div>
  <svg class="carousel-arrow" style="left:102px" width="14" height="22" viewBox="0 0 14 22" fill="none" stroke="#fff" stroke-width="2"><path d="M12 2L3 11l9 9"/></svg>
  <svg class="carousel-arrow" style="left:1085px" width="14" height="22" viewBox="0 0 14 22" fill="none" stroke="#fff" stroke-width="2"><path d="M2 2l9 9-9 9"/></svg>
  <div class="shot" role="img" aria-label="Machined brass parts on a blue surface" style="left:158px;top:248px;width:282px;height:238px;background:linear-gradient(135deg,#2b5fa8,#b28a5a 50%,#2a5aa0)"></div>
  <div class="shot" role="img" aria-label="Green anodized tool in a foam case" style="left:459px;top:248px;width:282px;height:288px;background:radial-gradient(circle at 40% 45%,#3fa63a 0,#2b2b2b 45%,#3a3a3a)"></div>
  <div class="shot" role="img" aria-label="Rows of machined aluminum rings" style="left:760px;top:248px;width:281px;height:238px;background:linear-gradient(135deg,#c9c9c7,#7d7a73 50%,#b6b3ab)"></div>
</section>

<section class="better">
  <svg class="abs" style="left:0;top:0" width="150" height="160" viewBox="0 0 150 160"><polygon points="0,0 125,0 148,40 0,150" fill="#1b8a1b"/></svg>
  <svg class="abs" style="left:1075px;top:240px" width="125" height="149" viewBox="0 0 125 149"><polygon points="125,0 125,149 40,149 2,95 10,85" fill="#1b8a1b"/></svg>
  <svg class="abs" style="left:160px;top:54px" width="395" height="282" viewBox="0 0 395 282">
    <defs><linearGradient id="weldGrad" x1="0" y1="0" x2="1" y2="1"><stop offset="0" stop-color="#14233f"/><stop offset=".5" stop-color="#3c6ab8"/><stop offset="1" stop-color="#1b2333"/></linearGradient></defs>
    <polygon role="img" aria-label="Welder at work with sparks and blue light" points="40,0 393,0 353,282 0,282" fill="url(#weldGrad)"/>
  </svg>
  <h2>HOW WE MAKE IT BETTER <svg width="50" height="18" viewBox="0 0 50 18" fill="none" stroke="#6cc23f" stroke-width="1.6"><path d="M0 6h38M0 12h38M36 2l12 7-12 7"/></svg></h2>
  <ul class="checks">
    <li><svg width="14" height="14" viewBox="0 0 14 14" fill="none" stroke="#222" stroke-width="1.3"><circle cx="7" cy="7" r="6"/><path d="M4 7l2 2 4-4"/></svg>With 100 years of combined knowledge and experience to draw upon, we find solutions.</li>
    <li><svg width="14" height="14" viewBox="0 0 14 14" fill="none" stroke="#222" stroke-width="1.3"><circle cx="7" cy="7" r="6"/><path d="M4 7l2 2 4-4"/></svg>Our vast experience across multiple industries gives us insight that is invaluable in creativity and foresight.</li>
    <li><svg width="14" height="14" viewBox="0 0 14 14" fill="none" stroke="#222" stroke-width="1.3"><circle cx="7" cy="7" r="6"/><path d="M4 7l2 2 4-4"/></svg>This real life experience brings a broader understanding of what works, and more importantly, what doesn't work, ultimately allowing us to make more informed decisions.</li>
  </ul>
  <div class="btn-dark">LEARN MORE</div>
</section>

<section class="caps">
  <div class="eyebrow">What can we do?</div>
  <h2 class="section-title">While this list covers much of our capabilities, it<br>is by no means exhaustive. You can always<br>contact us with specific requests.</h2>

  <div class="divider-v" style="left:427px;top:215px;height:340px"></div>
  <div class="divider-v" style="left:759px;top:215px;height:340px"></div>
  <div class="divider-h" style="left:157px;top:385px;width:885px"></div>

  <div class="cap" style="left:157px;top:205px">
    <svg class="ic" width="52" height="48" viewBox="0 0 52 48" fill="none" stroke="#222" stroke-width="1.4"><rect x="4" y="6" width="44" height="30" rx="2"/><path d="M2 40h48M16 14h20v16H16zM26 8v6" stroke="#1b8a1b"/></svg>
    <h3>CAD Design</h3>
    <p>Do you have something that needs to be created, but no method of capturing the design?</p>
    <svg class="go" width="22" height="12" viewBox="0 0 22 12" fill="none" stroke="#111" stroke-width="1.5"><path d="M0 6h20M15 1l5 5-5 5"/></svg>
  </div>
  <div class="cap" style="left:489px;top:205px">
    <svg class="ic" width="52" height="48" viewBox="0 0 52 48" fill="none" stroke="#222" stroke-width="1.4"><rect x="2" y="2" width="48" height="44" rx="3"/><path d="M2 11h48"/><path d="M20 22l-6 6 6 6M32 22l6 6-6 6M28 20l-4 16" stroke="#1b8a1b"/></svg>
    <h3>CAM Programming</h3>
    <p>Do you need programs for your machines? Perhaps we can help. We use the latest 3D CAM</p>
    <svg class="go" width="22" height="12" viewBox="0 0 22 12" fill="none" stroke="#111" stroke-width="1.5"><path d="M0 6h20M15 1l5 5-5 5"/></svg>
  </div>
  <div class="cap" style="left:819px;top:205px">
    <svg class="ic" width="52" height="48" viewBox="0 0 52 48" fill="none" stroke="#222" stroke-width="1.4"><rect x="2" y="10" width="42" height="26" rx="2"/><path d="M14 44h18M23 36v8"/><path d="M23 2l10 5v10l-10 5-10-5V7z" stroke="#1b8a1b"/></svg>
    <h3>FFF 3D Printing</h3>
    <p>Do you need a quick sample? Using Fused Filament Fabrication we can 3D print prototypes for</p>
    <svg class="go" width="22" height="12" viewBox="0 0 22 12" fill="none" stroke="#111" stroke-width="1.5"><path d="M0 6h20M15 1l5 5-5 5"/></svg>
  </div>

  <div class="cap" style="left:157px;top:408px">
    <svg class="ic" width="52" height="48" viewBox="0 0 52 48" fill="none" stroke="#222" stroke-width="1.4"><rect x="4" y="14" width="44" height="28" rx="2"/><path d="M2 44h48"/><circle cx="26" cy="10" r="7" stroke="#1b8a1b"/><path d="M23 18h6M26 4v-3" stroke="#1b8a1b"/></svg>
    <h3>Prototypes</h3>
    <p>Do you need a custom part, or test sample?<br>We can make custom, one-off parts such as racing components,</p>
    <svg class="go" width="22" height="12" viewBox="0 0 22 12" fill="none" stroke="#111" stroke-width="1.5"><path d="M0 6h20M15 1l5 5-5 5"/></svg>
  </div>
  <div class="cap" style="left:489px;top:408px">
    <svg class="ic" width="52" height="48" viewBox="0 0 52 48" fill="none" stroke="#222" stroke-width="1.4"><path d="M6 2h40v8H6zM20 10h12v10H20zM26 20v10"/><path d="M6 36l20 10 20-10-20-8z" stroke="#1b8a1b"/></svg>
    <h3>Vertical CNC Machining</h3>
    <p>with simultaneous 4th axis rotary<br>If you need parts processed through a vertical machining center, let us know.</p>
    <svg class="go" width="22" height="12" viewBox="0 0 22 12" fill="none" stroke="#111" stroke-width="1.5"><path d="M0 6h20M15 1l5 5-5 5"/></svg>
  </div>
  <div class="cap" style="left:819px;top:408px">
    <svg class="ic" width="52" height="48" viewBox="0 0 52 48" fill="none" stroke="#222" stroke-width="1.4"><path d="M10 2h24v8H10zM16 10h12v8H16zM22 18v8M14 22l16 6"/><path d="M6 38l16 8 16-8-16-8z" stroke="#1b8a1b"/></svg>
    <h3>CNC Turning</h3>
    <p>Collet or chuck work<br>If you need parts processed through a CNC lathe, let us know.</p>
    <svg class="go" width="22" height="12" viewBox="0 0 22 12" fill="none" stroke="#111" stroke-width="1.5"><path d="M0 6h20M15 1l5 5-5 5"/></svg>
  </div>

  <div class="btn-green" style="left:503px;top:625px;width:194px;height:38px">VIEW ALL CAPABILITIES</div>
</section>

<section class="contact">
  <h2>GET IN TOUCH WITH US</h2>
  <div class="field" style="top:114px">Name :</div>
  <div class="field" style="top:158px">Email :</div>
  <div class="field" style="top:202px">Phone :</div>
  <div class="field" style="top:246px;height:106px">Message :</div>
  <div class="btn-green">SUBMIT</div>
  <svg class="abs" style="left:548px;top:83px" width="430" height="283" viewBox="0 0 430 283">
    <defs><linearGradient id="teamGrad" x1="0" y1="0" x2="1" y2="1"><stop offset="0" stop-color="#d9dde0"/><stop offset=".45" stop-color="#c9d54a"/><stop offset="1" stop-color="#6b7a8c"/></linearGradient></defs>
    <polygon role="img" aria-label="Two workers in hard hats and safety vests in a factory" points="30,0 428,0 398,282 0,282" fill="url(#teamGrad)"/>
  </svg>
</section>

<footer class="site-footer">
  <div class="wordmark"><span class="sq"></span>TREMLA</div>
  <nav class="foot-nav">
    <span>HOME</span><span>|</span><span>CAPABILITIES</span><span>|</span><span>ABOUT US</span><span>|</span><span>GALLERY</span><span>|</span><span>WISDOM</span><span>|</span><span>CONTACT US</span>
  </nav>
  <div class="rule"></div>
  <div class="copyright">© Copyright 2022 Tremla | All rights reserved.</div>
  <div class="social"><span></span><span></span><span></span><span></span></div>
</footer>

</body>
</html>
```